Brisk Mend's Blow Their Mind Website

We own a group of cell phone and tablet repair shops in the bay area that is emerging into the mobile device insurance industry and want to develop a site that is clean, organized, and efficient at communicating who we are, the services we provide and the positive feedback we have been getting from our clients. As we enter into this new field of business, Our goal is to attract larger corporate accounts.

We want our home screen to have a big focus on the protection plan for the devices right away much like the home screen from these links:

http://www.velmorcove.com/

and also - https://us.keeplarnwick.com/smartphone-protection.html

We also need to make our repair services clear, here is a website of a company that does repair and we want to highlight both ends of the business.

ww.dolvafix.com

So the home screen will include the tab categories at the top of the screen
home/ protection /repair /about /contact

The first portion will be protection and as you scroll down there will be the next section about repair and following that will be information about the company.

Target Market(s)

Individuals that would be looking for pricing, clients that come to our store, but ultimately the heavy hitters we would want to attract would be larger corporate accounts so the message we want to communicate is professional, organized and credible in the services we provide.

Cell Phone

5+ page

Serif

34a6d7

Must have
• Eye catching, organized, with the wow factor that a business will look at our site and will be able to tell that we know what looks good and what grabs peoples attention. A large emphasis on the protection plan section like the links we provided and an organized home screen with the sections highlighted in the project description
• Tabs with links to different sections of the business such as protection that will go into detail about our protections plans and why our plan is best
• repair with a menu of the different prices we provide for different devices and services for that device
• an about us tab
• a contact us tab
Nice to have
• Artistic flow on the homescreen that the different sections flow together without looking too cookie cutter
• Wow factor
Should not have
• Clutter, confusion, disorganization, cheesy cookie cutter

```html
<!DOCTYPE html>
<html lang="en">
<head>
<meta charset="utf-8">
<title>Brisk Mend</title>
<link href="https://fonts.googleapis.com/css2?family=Montserrat:wght@400;600;700&family=Open+Sans:wght@400;600&display=swap" rel="stylesheet">
<style>
:root{
  --brand:#1aa8ec;
  --brand-dark:#1592d0;
  --ink:#2b2b2b;
  --muted:#8a8a8a;
  --white:#ffffff;
  --panel:rgba(40,40,40,0.82);
  --footer:#2e2e2e;
  --footer-text:#a9a9a9;
  --card:#f4f4f4;
}
*{box-sizing:border-box;margin:0;padding:0}
html,body{width:1200px;height:2772px;overflow:hidden}
body{font-family:"Open Sans",Arial,sans-serif;color:var(--ink);background:var(--white);position:relative}
h1,h2,h3,h4,.nav a,.btn,.price-box{font-family:"Montserrat",Arial,sans-serif}

/* header */
.site-header{position:absolute;top:0;left:0;width:1200px;height:96px;background:var(--white);display:flex;align-items:center;padding:0 160px}
.logo{display:flex;align-items:center;gap:12px;font-family:"Montserrat",Arial,sans-serif;font-weight:600;font-size:26px;color:var(--brand)}
.logo-dot{width:30px;height:30px;border-radius:50%;background:var(--brand)}
.nav{margin-left:auto;display:flex;gap:44px}
.nav a{font-size:13px;letter-spacing:1px;color:#7a7a7a;text-decoration:none;padding-bottom:8px;border-bottom:2px solid transparent}
.nav a.active{color:var(--brand);border-color:var(--brand)}

/* photo bands */
.band{position:absolute;left:0;width:1200px;overflow:hidden}
.photo{position:absolute;inset:0}
.hero{top:96px;height:524px}
.hero .photo{background:linear-gradient(100deg,#1b1b1d 0%,#2a2a2c 40%,#4a4438 70%,#1f2a1e 100%)}
.hero-copy{position:absolute;left:160px;top:152px;color:var(--white);width:380px}
.hero-copy h1{font-size:38px;font-weight:700;line-height:1.2;margin-bottom:20px}
.hero-copy p{font-size:14px;line-height:1.6;margin-bottom:18px}
.hero-copy ul{list-style:none;font-size:14px;line-height:1.7}
.price-box{position:absolute;left:708px;top:192px;width:252px;height:64px;background:var(--brand);color:var(--white);display:flex;align-items:center;justify-content:center;gap:8px;font-size:13px}
.price-box strong{font-size:34px;font-weight:700}
.btn{display:inline-block;text-decoration:none;font-size:13px;font-weight:600}
.btn-quote{position:absolute;left:708px;top:272px;width:252px;height:32px;line-height:32px;text-align:center;background:var(--brand-dark);color:var(--white)}

.repair{top:620px;height:520px}
.repair .photo{background:linear-gradient(180deg,#e9b88c 0%,#c99a7e 30%,#7b7478 60%,#3f4a55 100%)}
.about{top:1140px;height:520px}
.about .photo{background:linear-gradient(110deg,#2d3442 0%,#4b4b52 45%,#8b7a63 75%,#b3a489 100%)}

.info-panel{position:absolute;background:var(--panel);color:var(--white);padding:48px 40px}
.info-panel h2{font-size:24px;font-weight:600;line-height:1.3;margin-bottom:20px}
.info-panel p{font-size:13px;line-height:1.7;margin-bottom:26px;color:#e6e6e6}
.btn-light{background:var(--white);color:var(--ink);padding:9px 20px}
.repair .info-panel{left:160px;top:80px;width:368px;height:360px}
.about .info-panel{left:720px;top:80px;width:320px;height:340px;text-align:right}

/* testimonials */
.feedback{position:absolute;top:1660px;left:0;width:1200px;height:532px}
.feedback h2{text-align:center;font-size:26px;font-weight:600;margin-top:68px}
.cards{position:absolute;top:140px;left:160px;display:flex;gap:28px}
.card{width:418px;height:272px;background:var(--card);display:flex}
.card-photo{width:152px;height:100%;background:linear-gradient(180deg,#c9b7a6,#8d7668)}
.card:nth-child(2) .card-photo{background:linear-gradient(180deg,#c98c78,#7c3f36)}
.card-body{padding:22px 20px;flex:1}
.card-body h3{font-size:20px;font-weight:600;color:#555;margin-bottom:14px}
.card-body p{font-size:12px;line-height:1.65;color:var(--muted);margin-bottom:20px}
.card-role{font-size:11px;color:#b0b0b0}
.dots{position:absolute;top:456px;left:0;width:1200px;display:flex;justify-content:center;gap:12px}
.dots span{width:12px;height:12px;border-radius:50%;border:2px solid var(--brand)}
.dots span.on{background:var(--brand)}

/* call to action */
.cta{position:absolute;top:2192px;left:0;width:1200px;height:248px;background:var(--brand);color:var(--white);text-align:center;padding-top:56px}
.cta h2{font-size:24px;font-weight:600;margin-bottom:16px}
.cta p{font-size:14px;line-height:1.6;width:620px;margin:0 auto 28px}
.btn-contact{background:var(--white);color:var(--brand);padding:10px 26px}

/* footer */
.site-footer{position:absolute;top:2440px;left:0;width:1200px;height:332px;background:var(--footer);color:var(--footer-text);padding:76px 160px 0;display:flex}
.site-footer h4{color:var(--white);font-size:14px;font-weight:600;margin-bottom:16px}
.footer-brand{width:308px}
.footer-brand h4{font-size:22px}
.footer-brand p{font-size:11px;line-height:1.7;width:250px}
.footer-col{width:144px}
.footer-col ul{list-style:none;font-size:11px;line-height:1.85}
.footer-connect{width:240px;margin-left:52px}
.social{display:flex;gap:16px;margin-top:8px}
.social span{width:18px;height:18px;border-radius:50%;background:#6a6a6a}
</style>
</head>
<body>

<header class="site-header">
  <div class="logo"><span class="logo-dot"></span>Brisk Mend</div>
  <nav class="nav">
    <a href="#">HOME</a>
    <a href="#" class="active">PROTECT</a>
    <a href="#">ABOUT</a>
    <a href="#">CONTACT</a>
  </nav>
</header>

<section class="band hero">
  <div class="photo" role="img" aria-label="Hand holding a smartphone in a dark room"></div>
  <div class="hero-copy">
    <h1>PEACE OF<br>MIND</h1>
    <p>We don't care where you bought your phone, which carrier you have.</p>
    <ul>
      <li>Every cracked screen can be repaired fast</li>
      <li>Every lost phone can be replaced quickly</li>
      <li>Every device we cover is fully protected</li>
    </ul>
  </div>
  <div class="price-box">from <strong>$4.45</strong> per month</div>
  <a href="#" class="btn btn-quote">Get your quote now</a>
</section>

<section class="band repair">
  <div class="photo" role="img" aria-label="Hand holding a phone photographing a sunset over the sea"></div>
  <div class="info-panel">
    <h2>How do we repair things for you!</h2>
    <p>Bring any phone or tablet to our bay area shops and our certified technicians will diagnose it free, quote a fair price and fix most devices the same day.</p>
    <a href="#" class="btn btn-light">Learn More</a>
  </div>
</section>

<section class="band about">
  <div class="photo" role="img" aria-label="Person relaxing on a sofa while using a smartphone"></div>
  <div class="info-panel">
    <h2>Why Brisk Mend &amp;<br>Our services</h2>
    <p>Brisk Mend blends years of hands-on repair work with protection plans built for families, small teams and corporate fleets who need devices that simply keep working.</p>
    <a href="#" class="btn btn-light">Learn More</a>
  </div>
</section>

<section class="feedback">
  <h2>Clients Feedback</h2>
  <div class="cards">
    <article class="card">
      <div class="card-photo" role="img" aria-label="Portrait of client Dale Harmon"></div>
      <div class="card-body">
        <h3>Dale Harmon</h3>
        <p>The team replaced screens on our entire sales fleet in one afternoon. Clear pricing, friendly staff and every phone came back looking brand new.</p>
        <div class="card-role">Repair Manager</div>
      </div>
    </article>
    <article class="card">
      <div class="card-photo" role="img" aria-label="Portrait of client Marisol"></div>
      <div class="card-body">
        <h3>Marisol</h3>
        <p>I signed up for the protection plan after my first repair. When I dropped my tablet months later, the claim took minutes and the fix was free.</p>
        <div class="card-role">Store Owner</div>
      </div>
    </article>
  </div>
  <div class="dots"><span class="on"></span><span></span><span></span></div>
</section>

<section class="cta">
  <h2>Get an Appointment &amp; Repair Now!</h2>
  <p>Book a visit at any of our bay area shops and walk out with a working device, usually within the hour.</p>
  <a href="#" class="btn btn-contact">Contact Now</a>
</section>

<footer class="site-footer">
  <div class="footer-brand">
    <h4>Brisk Mend</h4>
    <p>Phone and tablet repair with protection plans for people and businesses across the bay area, backed by certified technicians and honest pricing.</p>
  </div>
  <div class="footer-col">
    <h4>Brisk Mend</h4>
    <ul><li>Home</li><li>About</li><li>Protection</li><li>Repair</li><li>Blog</li><li>Contact Us</li></ul>
  </div>
  <div class="footer-col">
    <h4>Explore</h4>
    <ul><li>Privacy</li><li>Terms of Service</li><li>Warranty</li><li>Careers</li><li>Press</li><li>Blog</li></ul>
  </div>
  <div class="footer-connect">
    <h4>Connect With Us</h4>
    <div class="social"><span></span><span></span><span></span><span></span><span></span></div>
  </div>
</footer>

</body>
</html>
```